Bright Arch Group business card

Bright Arch Group is the parent company of Bright Arch Building, Bright Arch Plumbing and Bright Arch Renovating. We require a sophisticated business card that covers all aspects of the building and plumbing space without using told or construction items.

Industry/Entity Type

Construction Company

Contact Information for Business Card

Gareth Pimley
Director
0472915083
gareth@brightarch.com.au
Www.brightarch.com.au

Font styles to use
Serif
Sans Serif

Colors
3176b5
ffce3e
0692cd
34a7d8
fbee3e
faa54b

Requirements
Must have
• Logo on front
• Logo and details on rear.
Nice to have
• Maybe water mark or shadow effect with logo
Should not have
• Tools or any construction associated items

```html
<!DOCTYPE html>
<html lang="en">
<head>
<meta charset="utf-8">
<title>Bright Arch Group — Business Card</title>
<link href="https://fonts.googleapis.com/css2?family=Arimo:wght@400;700&display=swap" rel="stylesheet">
<style>
  :root {
    --backdrop: #4d5157;
    --brand-blue: #1690cd;
    --brand-orange: #f58220;
    --paper: #ffffff;
    --card-w: 900px;
    --card-h: 500px;
  }
  * { box-sizing: border-box; margin: 0; padding: 0; }
  html, body {
    width: 1200px;
    height: 1200px;
    overflow: hidden;
    background: var(--backdrop);
    font-family: "Arimo", Arial, sans-serif;
  }
  .layout {
    width: 1200px;
    height: 1200px;
    display: flex;
    flex-direction: column;
    align-items: center;
    justify-content: center;
    gap: 60px;
  }
  .card {
    width: var(--card-w);
    height: var(--card-h);
    position: relative;
    overflow: hidden;
  }

  /* Back side: orange with brand name and website */
  .card--back {
    background: var(--brand-orange);
    display: flex;
    flex-direction: column;
    align-items: center;
    justify-content: center;
    gap: 26px;
    color: var(--paper);
  }
  .back-brand {
    font-size: 44px;
    font-weight: 400;
    letter-spacing: 6px;
    text-transform: uppercase;
  }
  .back-web {
    font-size: 20px;
    letter-spacing: 0.5px;
  }

  /* Front side: blue brand panel + white details */
  .card--front {
    display: flex;
    background: var(--paper);
  }
  .brand-panel {
    width: 48%;
    background: var(--brand-blue);
    display: flex;
    align-items: center;
    justify-content: center;
  }
  .brand-name {
    color: var(--paper);
    font-size: 34px;
    font-weight: 400;
    letter-spacing: 7px;
    text-transform: uppercase;
    text-align: center;
    line-height: 1.35;
  }
  .details {
    flex: 1;
    padding: 150px 0 0 62px;
  }
  .person-name {
    color: var(--brand-blue);
    font-size: 46px;
    font-weight: 400;
    letter-spacing: -0.5px;
    line-height: 1;
  }
  .person-role {
    color: var(--brand-orange);
    font-size: 22px;
    margin: 6px 0 0 4px;
  }
  .contact-list {
    list-style: none;
    margin: 30px 0 0 10px;
  }
  .contact-item {
    display: flex;
    align-items: center;
    gap: 10px;
    color: var(--brand-blue);
    font-size: 19px;
    height: 34px;
  }
  .contact-icon {
    width: 20px;
    height: 20px;
    flex: none;
  }
</style>
</head>
<body>
<main class="layout">

  <section class="card card--back" aria-label="Card back">
    <div class="back-brand">Bright Arch Group</div>
    <div class="back-web">www.brightarch.com.au</div>
  </section>

  <section class="card card--front" aria-label="Card front">
    <div class="brand-panel">
      <div class="brand-name">Bright Arch<br>Group</div>
    </div>
    <div class="details">
      <h1 class="person-name">Gareth Pimley</h1>
      <p class="person-role">Director</p>
      <ul class="contact-list">
        <li class="contact-item">
          <svg class="contact-icon" viewBox="0 0 24 24" aria-hidden="true">
            <path fill="#f58220" d="M6.6 10.8a15.1 15.1 0 0 0 6.6 6.6l2.2-2.2a1 1 0 0 1 1-.25 11.4 11.4 0 0 0 3.6.57 1 1 0 0 1 1 1V20a1 1 0 0 1-1 1A17 17 0 0 1 3 4a1 1 0 0 1 1-1h3.5a1 1 0 0 1 1 1c0 1.25.2 2.45.57 3.6a1 1 0 0 1-.25 1z"/>
          </svg>
          <span>0472915083</span>
        </li>
        <li class="contact-item">
          <svg class="contact-icon" viewBox="0 0 24 24" aria-hidden="true">
            <rect x="2" y="5" width="20" height="14" fill="#f58220"/>
            <path d="M2.5 5.5 12 13l9.5-7.5" fill="none" stroke="#fff" stroke-width="1.6"/>
          </svg>
          <span>gareth@brightarch.com.au</span>
        </li>
        <li class="contact-item">
          <svg class="contact-icon" viewBox="0 0 24 24" aria-hidden="true">
            <g fill="none" stroke="#f58220" stroke-width="1.8">
              <circle cx="12" cy="12" r="9"/>
              <ellipse cx="12" cy="12" rx="4" ry="9"/>
              <path d="M3 12h18M4.5 7.5h15M4.5 16.5h15"/>
            </g>
          </svg>
          <span>www.brightarch.com.au</span>
        </li>
      </ul>
    </div>
  </section>

</main>
</body>
</html>
```